Cosmetic Dental Advert For lift in busy CBD

We need a DIRECT RESPONSE advert designed for a cosmetic dentist that is placing adverts into a building lift.

OFFICE PROVIDES BRANDS ACCESS TO REACH HIGH INCOME PROFESSIONALS WITHIN PREMIUM BUSINESS ENVIRONMENTS

We are not advertising a specific clinic so we want people to go to the website that is advertised and ask for the free initial consultation.

You can reduce the amount of words / points to make it simpler to read.

Target Market(s)

Professional at work - seeing advert in a lift or foyer

Industry/Entity Type

Dental

Colors

Designer to choose colors to be used in the design.

Requirements
Must have
• The domain "www.grinvale47.com.au" must be very strong and encourage people to visit / search for it.
• The offer is a ["FREE Initial consultation" with voucher code "grinvale47"]
• The advert must be in Vector format.
• Apply the landing page corner image bottom right
Nice to have
• Provide a Male / Female version
• Emphasize the beautiful smile like in the sample
Should not have
• Must not be busy. This is a direct response so the viewer must get the call to action in 2 seconds

```html
<!DOCTYPE html>
<html lang="en">
<head>
<meta charset="utf-8">
<title>Transform your smile – Cosmetic Dentistry</title>
<link href="https://fonts.googleapis.com/css2?family=Lato:wght@400;700&family=Raleway:wght@400;500&display=swap" rel="stylesheet">
<style>
  :root {
    --page: #f3f3f5;
    --plus: #dcdce3;
    --pink: #e05aa8;
    --pink-soft: #e683c4;
    --lilac: #8b8fd6;
    --lilac-deep: #6f74c9;
    --navy: #262f7a;
    --blue: #3a58b8;
    --band: #121214;
    --white: #ffffff;
    --curl-shadow: #b9b9c2;
  }
  * { margin: 0; padding: 0; box-sizing: border-box; }
  html, body { width: 900px; height: 1200px; overflow: hidden; background: var(--page); }
  .advert {
    position: relative;
    width: 900px;
    height: 1200px;
    overflow: hidden;
    background: var(--page);
    font-family: "Lato", Arial, sans-serif;
  }
  .decor { position: absolute; inset: 0; }
  .portrait {
    position: absolute;
    left: 20px;
    top: 300px;
    width: 500px;
    height: 720px;
    border-radius: 240px 240px 0 0;
    background: linear-gradient(180deg, #5a3a2e 0%, #c99a86 35%, #2a2a30 70%, #1d1d22 100%);
  }
  .headline {
    position: absolute;
    left: 280px;
    top: 120px;
    font-family: "Raleway", Arial, sans-serif;
    font-weight: 500;
    color: var(--blue);
    font-size: 74px;
    line-height: 1.05;
  }
  .headline-smile {
    position: absolute;
    left: 500px;
    top: 300px;
    font-family: "Raleway", Arial, sans-serif;
    font-weight: 400;
    color: var(--white);
    font-size: 170px;
    line-height: 1;
    letter-spacing: -2px;
  }
  .service {
    position: absolute;
    left: 600px;
    top: 505px;
    font-family: "Raleway", Arial, sans-serif;
    color: var(--navy);
    font-size: 56px;
    line-height: 1.1;
  }
  .voucher {
    position: absolute;
    left: 680px;
    top: 770px;
    color: var(--blue);
    font-size: 34px;
    line-height: 1.2;
  }
  .offer-band {
    position: absolute;
    left: 40px;
    top: 955px;
    width: 600px;
    height: 245px;
    background: var(--band);
    color: var(--white);
    text-align: center;
    padding-top: 26px;
  }
  .offer-text { font-size: 46px; line-height: 1.1; }
  .offer-text .free { color: var(--pink); font-weight: 700; }
  .offer-url {
    margin-top: 18px;
    color: var(--pink);
    font-weight: 700;
    font-size: 54px;
    letter-spacing: -0.5px;
  }
  .page-curl { position: absolute; right: 0; bottom: 0; width: 300px; height: 140px; }
  .brand {
    position: absolute;
    right: 24px;
    bottom: 28px;
    font-family: "Lato", Arial, sans-serif;
    font-weight: 700;
    font-size: 30px;
    color: var(--blue);
  }
</style>
</head>
<body>
<main class="advert">
  <svg class="decor" width="900" height="1200" viewBox="0 0 900 1200" aria-hidden="true">
    <g fill="var(--plus)">
      <rect x="108" y="130" width="6" height="36"/><rect x="93" y="145" width="36" height="6"/>
      <rect x="338" y="48" width="5" height="30"/><rect x="326" y="60" width="30" height="5"/>
      <rect x="788" y="150" width="6" height="36"/><rect x="773" y="165" width="36" height="6"/>
      <rect x="130" y="330" width="5" height="30"/><rect x="118" y="342" width="30" height="5"/>
      <rect x="820" y="660" width="5" height="30"/><rect x="808" y="672" width="30" height="5"/>
    </g>
    <circle cx="480" cy="200" r="160" fill="var(--pink-soft)"/>
    <circle cx="650" cy="400" r="235" fill="var(--lilac)" opacity="0.9"/>
    <path d="M480 360 A160 160 0 0 0 560 60 A235 235 0 0 0 480 360 Z" fill="var(--lilac-deep)" opacity="0.55"/>
  </svg>

  <div class="portrait" role="img" aria-label="Photograph of a smiling woman in a dark blazer with arms folded"></div>

  <h1 class="headline">Transform<br>your</h1>
  <p class="headline-smile">smile</p>
  <p class="service">with<br>Cosmetic<br>Dentistry</p>

  <p class="voucher">Voucher code<br>“grinvale47”</p>

  <section class="offer-band">
    <p class="offer-text">For a <span class="free">free</span> initial<br>consultation visit:</p>
    <p class="offer-url">www.grinvale47.com.au</p>
  </section>

  <svg class="page-curl" viewBox="0 0 300 140" aria-hidden="true">
    <defs>
      <linearGradient id="fold" x1="0" y1="0" x2="1" y2="1">
        <stop offset="0" stop-color="#ffffff"/>
        <stop offset="1" stop-color="#d4d4dc"/>
      </linearGradient>
    </defs>
    <path d="M0 140 L300 20 L300 140 Z" fill="var(--white)"/>
    <path d="M0 140 C80 100 200 60 300 20 C250 40 140 120 0 140 Z" fill="var(--curl-shadow)" opacity="0.6"/>
    <path d="M300 20 C220 70 120 100 40 130 L300 0 Z" fill="url(#fold)"/>
  </svg>
  <p class="brand">BrightArc</p>
</main>
</body>
</html>
```